Business card for plumber

I need a business card for my plumbing company.
on it should:
Surname
position
E-mail
Telephone & mobile phone
Website
Please everything as placeholders / fantasy names.
We stand for high quality, hygiene and professionalism.

Colours:
# 606060 anthracite
# f7931e orange
# 2b89cc blue

Industry/Entity Type

Plumber

Contact Information for Business Card

folgt...

```html
<!DOCTYPE html>
<html lang="en">
<head>
<meta charset="UTF-8">
<title>Brunnfeld Haustechnik – Business Card</title>
<link href="https://fonts.googleapis.com/css2?family=Open+Sans:wght@400;600&family=Roboto+Condensed:wght@700&display=swap" rel="stylesheet">
<style>
  :root {
    --stage: #d6d6d4;
    --anthracite: #606060;
    --card-dark: #2d2d2e;
    --card-light: #ffffff;
    --orange: #f7931e;
    --blue: #2b89cc;
    --text-grey: #4a4a4a;
    --ghost: #efefef;
  }
  * { box-sizing: border-box; margin: 0; padding: 0; }
  html, body {
    width: 1200px; height: 675px; overflow: hidden;
    background: var(--stage);
  }
  .stage {
    position: relative; width: 1200px; height: 675px;
    display: flex; align-items: center; justify-content: center; gap: 60px;
  }
  .card {
    position: relative; width: 520px; height: 297px;
    border-radius: 18px; overflow: hidden;
    box-shadow: 0 6px 18px rgba(0,0,0,0.18);
  }

  /* Front */
  .card--front {
    background: var(--card-dark);
    display: flex; flex-direction: column; align-items: center; justify-content: center;
    gap: 30px;
  }
  .wordmark {
    display: flex; align-items: center; gap: 14px;
  }
  .wordmark__dot {
    width: 30px; height: 30px; border-radius: 50%; background: var(--orange); flex: none;
  }
  .wordmark__name {
    font-family: "Roboto Condensed", sans-serif; font-weight: 700;
    color: var(--blue); text-transform: uppercase; letter-spacing: 1px;
    font-size: 34px; line-height: 1;
  }
  .services {
    font-family: "Roboto Condensed", sans-serif; font-weight: 700;
    color: var(--orange); font-size: 15px; letter-spacing: 0.8px;
    text-transform: uppercase;
  }

  /* Back */
  .card--back { background: var(--card-light); }
  .card--back .wordmark { position: absolute; left: 34px; top: 36px; }
  .card--back .wordmark__dot { width: 22px; height: 22px; }
  .card--back .wordmark__name { font-size: 25px; }
  .contact {
    position: absolute; left: 34px; top: 124px;
    list-style: none; display: flex; flex-direction: column; gap: 9px;
    font-family: "Open Sans", sans-serif; font-size: 13px; color: var(--text-grey);
  }
  .contact__item { display: flex; align-items: center; gap: 9px; }
  .contact__icon { width: 14px; height: 14px; flex: none; }
  .person {
    position: absolute; right: 34px; top: 178px; text-align: right;
    font-family: "Open Sans", sans-serif;
  }
  .person__name { color: var(--orange); font-size: 24px; font-weight: 600; line-height: 1.05; }
  .person__role { color: var(--blue); font-size: 13px; }
  .ghost-mark {
    position: absolute; right: 150px; bottom: 30px;
    font-family: "Roboto Condensed", sans-serif; font-weight: 700;
    font-size: 40px; color: var(--ghost); text-transform: uppercase; line-height: 1;
  }
  .edge-band {
    position: absolute; left: 0; right: 0; bottom: 0; height: 14px; display: flex;
  }
  .edge-band__blue { flex: 0 0 58%; background: var(--blue); }
  .edge-band__orange { flex: 1; background: var(--orange); }
</style>
</head>
<body>
<main class="stage">
  <section class="card card--front" aria-label="Card front">
    <div class="wordmark">
      <span class="wordmark__dot"></span>
      <span class="wordmark__name">Brunnfeld Haustechnik</span>
    </div>
    <p class="services">Plumbing • Heating 24h Emergency Service • Maintenance</p>
  </section>

  <section class="card card--back" aria-label="Card back">
    <div class="wordmark">
      <span class="wordmark__dot"></span>
      <span class="wordmark__name">Brunnfeld Haustechnik</span>
    </div>

    <ul class="contact">
      <li class="contact__item">
        <svg class="contact__icon" viewBox="0 0 14 14"><circle cx="7" cy="7" r="7" fill="var(--blue)"/><path d="M4.3 3.6l1.5-.2.7 1.7-.9.7c.5 1 1.2 1.7 2.2 2.2l.7-.9 1.7.7-.2 1.5c-3.3.2-5.9-2.4-5.7-5.7z" fill="#fff"/></svg>
        <span>555.014.2290</span>
      </li>
      <li class="contact__item">
        <svg class="contact__icon" viewBox="0 0 14 14"><circle cx="7" cy="7" r="7" fill="var(--blue)"/><rect x="3.5" y="4.5" width="7" height="5" fill="none" stroke="#fff" stroke-width="1"/><path d="M3.5 4.7L7 7.3l3.5-2.6" fill="none" stroke="#fff" stroke-width="1"/></svg>
        <span>Email ID</span>
      </li>
      <li class="contact__item">
        <svg class="contact__icon" viewBox="0 0 14 14"><circle cx="7" cy="7" r="7" fill="var(--blue)"/><circle cx="7" cy="7" r="3.6" fill="none" stroke="#fff" stroke-width="1"/><path d="M3.4 7h7.2M7 3.4c-1.6 2-1.6 5.2 0 7.2M7 3.4c1.6 2 1.6 5.2 0 7.2" fill="none" stroke="#fff" stroke-width="0.8"/></svg>
        <span>brunnfeldhaustechnik.com</span>
      </li>
    </ul>

    <span class="ghost-mark" aria-hidden="true">Brunnfeld</span>

    <div class="person">
      <p class="person__name">NAME</p>
      <p class="person__role">Designation</p>
    </div>

    <div class="edge-band" aria-hidden="true">
      <span class="edge-band__blue"></span>
      <span class="edge-band__orange"></span>
    </div>
  </section>
</main>
</body>
</html>
```